New career and executive coaching business needs a business card design including logo

Company name: 'Harbourline Career Partners.' The aim of my coaching engagements is to help people improve their communication in the workplace and achieve their career goals. The process involves working with individuals to help them uncover their strengths and talents, then leverage those to improve their working lives. The Tellwood Inventory is the starting point to the process. I am after an exciting and interesting business card design (including logo)which is professional yet will still get people's attention.

Industry/Entity Type

Business

Contact Information for Business Card

Name: Gavin Holloway
Position: Owner
Address: 58 Pellimore Cres, Wardell Vic 3197
Phone: 0481937145
Website: harbourlinecareer.com.au
Email: gavin@hcp.com.au

Colors
33a6d7
00a990
0355a3
3176b5

Requirements
Must have
• logo

```html
<!DOCTYPE html>
<html lang="en">
<head>
<meta charset="utf-8">
<title>Harbourline Career Partners – Business Card</title>
<link rel="stylesheet" href="https://fonts.googleapis.com/css2?family=Montserrat:wght@500;700&display=swap">
<style>
  :root {
    --canvas: #ffffff;
    --card: #e6e7e8;
    --navy: #0355a3;
    --mid-blue: #3176b5;
    --sky: #33a6d7;
    --teal: #00a990;
    --ink: #231f20;
    --faint-sky: rgba(51, 166, 215, 0.35);
    --shadow: rgba(0, 0, 0, 0.35);
  }
  * { box-sizing: border-box; margin: 0; padding: 0; }
  html, body {
    width: 1200px; height: 900px; overflow: hidden;
    background: var(--canvas);
    font-family: "Montserrat", Arial, sans-serif;
    color: var(--ink);
  }
  .canvas { position: relative; width: 1200px; height: 900px; }
  .card {
    position: absolute; top: 381px;
    width: 378px; height: 219px;
    background: var(--card);
    box-shadow: 3px 3px 3px var(--shadow);
    overflow: hidden;
  }
  .card--front { left: 189px; }
  .card--back { left: 621px; }
  .band {
    position: absolute; left: 0; width: 100%; height: 18px;
    background: linear-gradient(to right, var(--mid-blue) 50%, var(--sky) 50%);
  }
  .band--top { top: 0; }
  .band--bottom { bottom: 0; }

  .brand {
    position: absolute; left: 126px; top: 44px;
    width: 126px; height: 112px;
    display: flex; flex-direction: column; align-items: center; justify-content: center; gap: 10px;
  }
  .brand__dot {
    width: 60px; height: 60px; border-radius: 50%;
    background: var(--teal);
  }
  .brand__name {
    font-weight: 700; font-size: 14px; color: var(--navy);
    white-space: nowrap;
  }
  .website {
    position: absolute; left: 0; top: 180px; width: 100%;
    text-align: center; font-size: 11px; letter-spacing: 2.6px; font-weight: 500;
  }

  .person { position: absolute; right: 27px; top: 41px; text-align: right; }
  .person__name { font-weight: 700; font-size: 13px; color: var(--navy); }
  .person__role { font-weight: 700; font-size: 8.5px; letter-spacing: 1px; margin-top: 1px; }

  .contacts { position: absolute; left: 41px; top: 99px; list-style: none; }
  .contact {
    display: flex; align-items: center; gap: 16px;
    height: 21px; margin-bottom: 9px;
    font-size: 9px; font-weight: 500;
  }
  .contact__icon {
    width: 21px; height: 21px; background: var(--teal);
    display: flex; align-items: center; justify-content: center;
  }
  .contact__icon svg { width: 13px; height: 13px; fill: #fff; }

  .faint-mark {
    position: absolute; left: 256px; top: 96px;
    width: 85px; height: 75px;
    display: flex; align-items: center; justify-content: center;
  }
  .faint-mark__dot { width: 72px; height: 72px; border-radius: 50%; background: var(--faint-sky); }
</style>
</head>
<body>
<main class="canvas">

  <section class="card card--front" aria-label="Card front">
    <div class="band band--top"></div>
    <div class="brand">
      <span class="brand__dot"></span>
      <span class="brand__name">Harbourline</span>
    </div>
    <p class="website">harbourlinecareer.com.au</p>
    <div class="band band--bottom"></div>
  </section>

  <section class="card card--back" aria-label="Card back">
    <div class="band band--top"></div>
    <div class="person">
      <p class="person__name">Gavin Holloway</p>
      <p class="person__role">OWNER</p>
    </div>
    <ul class="contacts">
      <li class="contact">
        <span class="contact__icon">
          <svg viewBox="0 0 24 24" aria-hidden="true"><path d="M6.6 10.8a15.1 15.1 0 0 0 6.6 6.6l2.2-2.2a1 1 0 0 1 1-.25 11.4 11.4 0 0 0 3.6.57 1 1 0 0 1 1 1V20a1 1 0 0 1-1 1A17 17 0 0 1 3 4a1 1 0 0 1 1-1h3.5a1 1 0 0 1 1 1c0 1.25.2 2.45.57 3.57a1 1 0 0 1-.25 1z"/></svg>
        </span>
        <span>0481937145</span>
      </li>
      <li class="contact">
        <span class="contact__icon">
          <svg viewBox="0 0 24 24" aria-hidden="true"><path d="M3 5h18v14H3z M5 7v10h14V7l-7 5z" fill-rule="evenodd"/></svg>
        </span>
        <span>gavin@hcp.com.au</span>
      </li>
      <li class="contact">
        <span class="contact__icon">
          <svg viewBox="0 0 24 24" aria-hidden="true"><path d="M12 2a7 7 0 0 0-7 7c0 5.2 7 13 7 13s7-7.8 7-13a7 7 0 0 0-7-7zm0 9.5A2.5 2.5 0 1 1 12 6.5a2.5 2.5 0 0 1 0 5z"/></svg>
        </span>
        <span>58 Pellimore Cres, Wardell Vic 3197</span>
      </li>
    </ul>
    <div class="faint-mark" aria-hidden="true">
      <span class="faint-mark__dot"></span>
    </div>
    <div class="band band--bottom"></div>
  </section>

</main>
</body>
</html>
```